Simple, bright, clean website - 3 pages, easy to update with WordPress!

I want to update my website (brevatlo.com) with a brighter/cleaner interface. It is quite dark right now. I would like it to be similar to a partner site (https://www.velmo-482.com/). White with some orange highlights (matching the logo). I want to be able to easily update the site content. There should be 3 main pages: About, Services, Contact. I also like a design similar to tarnop.com

Target Market(s)

Anyone using technology to achieve business goals.

Industry/Entity Type

Managed Service Provider (IT)

Coding

Coded - Design and coding required

Number of Pages Required

3 page

Colors
F0912C
F2A743
F7CA91
FBE8D2
FDF5EE

Requirements
Must have
• Links to standard social media apps like LinkedIn, Facebook, etc.. Easy to edit and add pages.

```html
<!DOCTYPE html>
<html lang="en">
<head>
<meta charset="utf-8">
<title>Brevatlo Consulting</title>
<link href="https://fonts.googleapis.com/css2?family=Heebo:wght@300;400;500;700;800&family=Nunito+Sans:wght@400;600;700&family=Montserrat:wght@500;700&display=swap" rel="stylesheet">
<style>
:root{
  --orange:#F0912C;
  --orange-2:#F2A743;
  --orange-3:#F7CA91;
  --orange-4:#FBE8D2;
  --cream:#FDF9F2;
  --ink:#1d1d1d;
  --muted:#555;
  --footer:#2a1d0b;
  --white:#fff;
}
*{margin:0;padding:0;box-sizing:border-box}
html,body{width:1200px;height:3454px;overflow:hidden}
body{position:relative;background:var(--cream);font-family:"Heebo",sans-serif;color:var(--ink)}
.abs{position:absolute}
a{color:inherit;text-decoration:none}

/* header */
.site-header{position:absolute;left:0;top:0;width:1200px;height:120px;background:var(--white)}
.brand{position:absolute;display:flex;align-items:center;gap:10px;font-family:"Heebo",sans-serif;font-weight:300;color:#666}
.brand-dot{width:18px;height:18px;border-radius:50%;background:var(--orange)}
.site-header .brand{left:74px;top:30px;font-size:50px}
.topbar{position:absolute;top:20px;right:97px;display:flex;gap:34px;font-size:15px;font-weight:500;color:#333}
.topbar span{display:flex;align-items:center;gap:6px}
.nav{position:absolute;top:72px;left:668px;display:flex;gap:28px;font-size:16px;color:#444}
.btn-connect{position:absolute;left:949px;top:60px;width:163px;height:46px;background:var(--orange);color:#fff;font-weight:700;font-size:16px;display:flex;align-items:center;justify-content:center;border-radius:3px}

/* hero */
.hero{position:absolute;left:0;top:120px;width:1200px;height:621px;overflow:hidden;background:linear-gradient(100deg,#6e4d14 0%,#9a6e1e 45%,#b8851f 70%,#a87618 100%)}
.hero h1{position:absolute;left:119px;top:140px;color:#fff;font-weight:300;font-size:62px;line-height:70px}
.hero h1 strong{font-weight:700}
.hero p{position:absolute;left:119px;top:310px;color:#fff;font-size:20px}
.btn-pill{position:absolute;display:flex;align-items:center;justify-content:center;border-radius:30px;background:var(--orange);color:#fff}
.hero .btn-pill{left:119px;top:367px;width:183px;height:55px;font-size:21px}
.hero-ring{position:absolute;left:673px;top:118px}

/* about */
.about-photo{position:absolute;left:120px;top:863px;width:494px;height:488px;border-radius:12px;background:linear-gradient(135deg,#cfd3cf,#8d8f86 60%,#5e5d58);box-shadow:0 8px 20px rgba(0,0,0,.2)}
.eyebrow{font-size:18px;color:var(--orange)}
.about-text{position:absolute;left:686px;top:912px;width:395px}
.about-bar{position:absolute;left:668px;top:917px;width:3px;height:72px;background:var(--orange)}
.about-text h2{font-weight:400;font-size:48px;line-height:58px;margin-bottom:14px}
.about-text p{font-family:"Nunito Sans",sans-serif;font-size:14px;line-height:24px;color:#333;margin-bottom:14px}
.about-text .btn-pill{position:static;width:171px;height:50px;font-size:16px;margin-top:22px}

/* services */
.services{position:absolute;left:0;top:1472px;width:1200px;height:624px;background:linear-gradient(120deg,#c98f22,#d59a2a 50%,#c68b1f)}
.section-head{position:absolute;left:0;width:1200px;text-align:center}
.section-head .eyebrow{font-size:19px}
.section-head h2{font-weight:400;font-size:48px;line-height:56px}
.section-head i{display:block;width:88px;height:3px;margin:14px auto 0;background:var(--orange)}
.services .section-head{top:58px;color:#fff}
.services .section-head .eyebrow{color:#fff}
.services .section-head i{background:#fff}
.svc-card{position:absolute;width:247px;height:219px;background:#fff;border-radius:4px;text-align:center}
.svc-icon{position:absolute;left:77px;top:-53px;width:94px;height:94px;border-radius:50%;background:#fff;border:6px solid var(--orange);display:flex;align-items:center;justify-content:center}
.svc-card h3{margin-top:60px;font-weight:400;font-size:26px}
.svc-card p{font-family:"Nunito Sans",sans-serif;font-size:14px;line-height:21px;color:#555;margin:6px 20px 0}
.svc-btn{display:inline-block;margin-top:14px;width:118px;height:35px;line-height:35px;border-radius:20px;background:#999;color:#fff;font-size:14px}
.svc-btn.active{background:var(--orange)}
.arrow{position:absolute;top:1796px;width:40px;height:40px;border-radius:50%;display:flex;align-items:center;justify-content:center}

/* reviews */
.reviews-head{top:2162px}
.review{position:absolute;top:2299px;width:464px;height:285px;background:#fff;border-radius:6px;box-shadow:0 4px 18px rgba(0,0,0,.06)}
.review p{position:absolute;left:50px;top:50px;width:370px;font-family:"Nunito Sans",sans-serif;font-size:15px;line-height:26.5px;color:#555}
.review .avatar{position:absolute;left:51px;top:176px;width:52px;height:52px;border-radius:50%;background:linear-gradient(#8a7a70,#3a3230)}
.review .name{position:absolute;left:127px;top:183px;font-size:16px}
.review .role{position:absolute;left:127px;top:205px;font-size:15px;color:#888}
.review .quote{position:absolute;left:368px;top:196px;font-family:"Heebo",sans-serif;font-weight:800;font-size:90px;line-height:60px;color:var(--orange)}

/* contact form */
.contact h2{position:absolute;left:0;width:1200px;top:2705px;text-align:center;font-family:"Montserrat",sans-serif;font-weight:700;font-size:33px}
.field{position:absolute;width:314px;height:47px;border:2px solid #d6d6d6;background:#fff;font-size:17px;color:#555;padding:12px 18px}
.field.message{height:119px}
.btn-outline{position:absolute;left:516px;top:3008px;width:168px;height:47px;border:2px solid var(--orange);border-radius:26px;display:flex;align-items:center;justify-content:center;font-family:"Montserrat",sans-serif;font-weight:700;font-size:16px}

/* footer */
.site-footer{position:absolute;left:0;top:3118px;width:1200px;height:336px;background:var(--footer);color:#fff;font-family:"Montserrat",sans-serif}
.foot-col{position:absolute;top:72px}
.foot-col h4{font-size:20px;font-weight:700;margin-bottom:12px}
.foot-col li{list-style:none;font-size:14px;font-weight:500;line-height:27px}
.foot-contact div{display:flex;gap:10px;font-size:14px;margin-bottom:14px;align-items:flex-start}
.foot-logo{position:absolute;left:807px;top:67px;width:218px;height:60px;background:#fff}
.foot-logo .brand{left:14px;top:6px;font-size:38px}
.socials{position:absolute;left:875px;top:164px;display:flex;gap:6px}
.socials span{width:33px;height:33px;border-radius:50%;border:1.5px solid #fff}
.copyright{position:absolute;left:0;bottom:20px;width:1200px;text-align:center;font-size:14px;padding-top:14px}
</style>
</head>
<body>

<header class="site-header">
  <div class="brand">brevatlo<span class="brand-dot"></span></div>
  <div class="topbar">
    <span><svg width="13" height="13" viewBox="0 0 24 24" fill="#333"><path d="M6.6 10.8a15 15 0 006.6 6.6l2.2-2.2a1 1 0 011-.25 11.4 11.4 0 003.6.57 1 1 0 011 1V20a1 1 0 01-1 1A17 17 0 013 4a1 1 0 011-1h3.5a1 1 0 011 1c0 1.25.2 2.45.57 3.57a1 1 0 01-.25 1z"/></svg>555-014-2290</span>
    <span><svg width="13" height="13" viewBox="0 0 24 24" fill="#333"><circle cx="12" cy="7" r="5"/><path d="M2 22c0-6 4.5-9 10-9s10 3 10 9z"/></svg>client login</span>
  </div>
  <nav class="nav"><a>About</a><a>Services ⌄</a><a>Contact Us</a></nav>
  <a class="btn-connect">Connect My Tech</a>
</header>

<section class="hero" role="img" aria-label="Team of consultants working together in an office, warm orange tint">
  <h1>The Leading<br><strong>Consulting</strong> Firm</h1>
  <p>We advise orgnizations in value creation strategies</p>
  <a class="btn-pill">Learn More</a>
  <svg class="hero-ring" width="410" height="410" viewBox="0 0 410 410">
    <circle cx="205" cy="205" r="196" fill="none" stroke="#F0912C" stroke-width="16"/>
    <circle cx="205" cy="205" r="172" fill="#d9dde3"/>
  </svg>
  <div class="abs" role="img" aria-label="Smiling support agent wearing a headset" style="left:706px;top:151px;width:344px;height:344px;border-radius:50%;background:linear-gradient(160deg,#e8ebef,#a9b4c4 60%,#5a6e8c)"></div>
</section>

<section class="about">
  <div class="about-photo" role="img" aria-label="Two colleagues shaking hands across an office desk"></div>
  <div class="about-bar"></div>
  <div class="about-text">
    <div class="eyebrow">Brevatlo Consulting</div>
    <h2>About Us</h2>
    <p>Lorem ipsum is simply dummy text of the printing and typesetting industry. Lorem Ipsum has been the industry's standard dummy text ever since the 1500s, when an unknown printer.</p>
    <p>when an unknown printer took a galley of type and scrambled it to make a type specimen book. It has survived not only five centuries, but also the leap into electronic typesetting.</p>
    <a class="btn-pill">LEARN MORE</a>
  </div>
</section>

<section class="services" role="img" aria-label="Office team background with orange overlay">
  <div class="section-head">
    <div class="eyebrow">Brevatlo Consulting</div>
    <h2>Our Services</h2><i></i>
  </div>
</section>

<svg width="0" height="0" style="position:absolute"><defs>
  <g id="gear"><circle cx="20" cy="20" r="15" fill="none" stroke="currentColor" stroke-width="3"/><circle cx="20" cy="20" r="7" fill="none" stroke="currentColor" stroke-width="3"/><g stroke="currentColor" stroke-width="3"><line x1="20" y1="2" x2="20" y2="8"/><line x1="20" y1="32" x2="20" y2="38"/><line x1="2" y1="20" x2="8" y2="20"/><line x1="32" y1="20" x2="38" y2="20"/></g></g>
</defs></svg>

<div class="svc-card" style="left:82px;top:1713px"><div class="svc-icon"><svg width="40" height="40" style="color:#777"><use href="#gear"/></svg></div><h3>Services</h3><p>Lorem ipsum is simply dummy text of the printing</p><a class="svc-btn">Read More</a></div>
<div class="svc-card" style="left:345px;top:1745px"><div class="svc-icon"><svg width="40" height="40" style="color:#F0912C"><use href="#gear"/></svg></div><h3>Services</h3><p>Lorem ipsum is simply dummy text of the printing</p><a class="svc-btn active">Read More</a></div>
<div class="svc-card" style="left:608px;top:1713px"><div class="svc-icon"><svg width="40" height="40" style="color:#777"><use href="#gear"/></svg></div><h3>Services</h3><p>Lorem ipsum is simply dummy text of the printing</p><a class="svc-btn">Read More</a></div>
<div class="svc-card" style="left:871px;top:1738px"><div class="svc-icon"><svg width="40" height="40" style="color:#777"><use href="#gear"/></svg></div><h3>Services</h3><p>Lorem ipsum is simply dummy text of the printing</p><a class="svc-btn">Read More</a></div>

<div class="arrow" style="left:28px;border:2px solid #fff"><svg width="14" height="14" viewBox="0 0 14 14"><path d="M9 1 3 7l6 6" fill="none" stroke="#fff" stroke-width="2"/></svg></div>
<div class="arrow" style="left:1131px;background:#2b2b2b"><svg width="14" height="14" viewBox="0 0 14 14"><path d="M5 1l6 6-6 6" fill="none" stroke="#fff" stroke-width="2"/></svg></div>

<section class="reviews">
  <div class="section-head reviews-head">
    <div class="eyebrow" style="color:#222">Brevatlo Consulting</div>
    <h2>Our Client Reviews</h2><i></i>
  </div>
  <article class="review" style="left:120px">
    <p>Lorem ipsum is simply dummy text of the printing and typesetting industry. Lorem Ipsum has been the industry's standard dummy text ever since the 1500s, when an unknown printer.</p>
    <div class="avatar" role="img" aria-label="Client portrait"></div>
    <div class="name">MAREN OLTBY</div><div class="role">Manager</div>
    <div class="quote">”</div>
  </article>
  <article class="review" style="left:617px">
    <p>Lorem ipsum is simply dummy text of the printing and typesetting industry. Lorem Ipsum has been the industry's standard dummy text ever since the 1500s, when an unknown printer.</p>
    <div class="avatar" role="img" aria-label="Client portrait"></div>
    <div class="name">MAREN OLTBY</div><div class="role">Manager</div>
    <div class="quote">”</div>
  </article>
</section>

<section class="contact">
  <h2>GET IN TOUCH</h2>
  <div class="field" style="left:273px;top:2779px">Your Name</div>
  <div class="field" style="left:273px;top:2851px">Email Address</div>
  <div class="field" style="left:273px;top:2923px">Phone</div>
  <div class="field" style="left:612px;top:2779px">Subject</div>
  <div class="field message" style="left:612px;top:2851px"></div>
  <a class="btn-outline">LEARN MORE</a>
</section>

<footer class="site-footer">
  <div class="foot-col" style="left:132px"><h4>COMPANY</h4><ul><li>Home</li><li>About Us</li><li>Solutions</li><li>Services</li><li>Support</li></ul></div>
  <div class="foot-col" style="left:343px"><h4>RESOURCES</h4><ul><li>Testimonials</li><li>Sitemap</li><li>Career</li><li>Cotact Us</li><li>Tearms</li></ul></div>
  <div class="foot-col foot-contact" style="left:545px"><h4>CONTACT US</h4>
    <div><svg width="12" height="16" viewBox="0 0 12 16"><path d="M6 0a6 6 0 016 6c0 4-6 10-6 10S0 10 0 6a6 6 0 016-6z" fill="#fff"/><circle cx="6" cy="6" r="2.2" fill="#2a1d0b"/></svg><span>48 Harlow Lane #4B<br>Austin 73301 TX</span></div>
    <div><svg width="14" height="14" viewBox="0 0 24 24" fill="#fff"><path d="M6.6 10.8a15 15 0 006.6 6.6l2.2-2.2a1 1 0 011-.25 11.4 11.4 0 003.6.57 1 1 0 011 1V20a1 1 0 01-1 1A17 17 0 013 4a1 1 0 011-1h3.5a1 1 0 011 1c0 1.25.2 2.45.57 3.57a1 1 0 01-.25 1z"/></svg><span>(555) 010 2040</span></div>
    <div><svg width="15" height="12" viewBox="0 0 15 12"><rect x=".5" y=".5" width="14" height="11" fill="none" stroke="#fff"/><path d="M.5.5l7 6 7-6" fill="none" stroke="#fff"/></svg><span>info@brevatlo.com</span></div>
  </div>
  <div class="foot-logo"><div class="brand">brevatlo<span class="brand-dot"></span></div></div>
  <div class="socials" aria-label="Social media links"><span></span><span></span><span></span><span></span></div>
  <div class="copyright">© 2024 Brevatlo. All Rights are Reserved.</div>
</footer>

</body>
</html>
```